Tollo is the place for Used Car Inspections

Tollo ONLY sells Used Car Inspections.

We need a website that tells that story simply.

Please be original and don't just copy my mockup. I'm not a designer.

Reason: Too few designers(<10)...too many weak designs(>80). I have subsequently revised my brief, uploaded more defined mockup and have tried to inspire some originality. I have also invited add designs, some who have declined. Any suggestions. Any suggestions?

Reason: Still waiting on original designs

Target Market(s)

Car Buyers

Industry/Entity Type

Used Car

Logo Text

Tollo

Number of Pages Required

5+ page

Font styles to use
Sans Serif

Colors
33a6d7
ffc214

Requirements
Must have
• Why Tollo?
• -Top 5 Questions
• Tollo Certified
• -Graphic detailing inspection
• How it Works
• -Graphic-- 1. Find a Location 2. Personal/Vehicle Info Form 3. Purchase
• -Get a Tollo Inspection
• Get a Tollo Inspection
• -Find a Location
• -Personal/Vehicle info Form
• -Purchase
• Become a Tollo Dealer
• -Form
• -Upload Credentials
• About Us
• Contact Us
• Term & Conditions
• Privacy
• FAQ
• Press
• Social Media
Nice to have
• Customer feedback-Quorra
Should not have
• Not sure

```html
<!DOCTYPE html>
<html lang="en">
<head>
<meta charset="utf-8">
<title>Tollo – Used Car Inspections</title>
<link href="https://fonts.googleapis.com/css2?family=Open+Sans:wght@400;600;700&family=Montserrat:wght@700&display=swap" rel="stylesheet">
<style>
:root{
  --blue:#33a6d7;
  --yellow:#ffc214;
  --dark:#1d1d1d;
  --ink:#222;
  --muted:#555;
  --white:#fff;
}
*{box-sizing:border-box;margin:0;padding:0}
html,body{width:774px;height:1200px;overflow:hidden;background:var(--white)}
body{font-family:"Open Sans",Arial,sans-serif;color:var(--ink);position:relative}
.site-header{position:absolute;top:0;left:0;width:774px;height:58px;background:var(--blue)}
.brand{position:absolute;left:18px;top:10px;display:flex;align-items:center;gap:7px}
.brand-dot{width:26px;height:26px;border-radius:50%;background:var(--yellow)}
.brand-name{font-family:"Montserrat",Arial,sans-serif;font-weight:700;font-size:22px;color:var(--white)}
.header-phone{position:absolute;right:40px;top:6px;font-weight:700;font-size:12px;color:var(--yellow)}
.main-nav{position:absolute;right:40px;top:30px;display:flex;gap:18px}
.main-nav a{color:var(--white);text-decoration:none;font-size:10px;font-weight:600;text-transform:uppercase}
.hero{position:absolute;top:58px;left:0;width:774px;height:212px;background:#151515}
.hero-photo{position:absolute;left:142px;top:10px;width:490px;height:192px;background:linear-gradient(135deg,#d9d9d9,#6d6d6d 55%,#2a2a2a)}
.intro{position:absolute;top:308px;left:115px;width:560px}
.intro h1{font-size:22px;font-weight:700;color:var(--ink);margin-bottom:8px}
.intro p{font-size:9.5px;line-height:1.45;color:var(--muted)}
.features{position:absolute;top:408px;left:115px;width:560px;height:112px}
.feature-photo{position:absolute;left:0;top:0;width:160px;height:112px;background:linear-gradient(135deg,#e6ecef,#9db3bf)}
.feature-list{position:absolute;left:188px;top:12px;display:grid;grid-template-columns:168px 168px;gap:10px 20px;list-style:none}
.feature-list li{height:22px;background:var(--blue);color:var(--white);font-size:8.5px;display:flex;align-items:center;padding-left:8px;gap:6px}
.feature-list li::before{content:"";width:7px;height:7px;background:var(--white)}
.steps{position:absolute;top:550px;left:0;width:774px;height:200px;background:var(--yellow)}
.step{position:absolute;height:72px}
.step h3{font-size:14px;font-weight:700;margin-bottom:4px;white-space:nowrap}
.step p{font-size:8.5px;line-height:1.4;color:#333}
.step .more{position:absolute;right:0;bottom:0;font-size:8.5px;color:#333}
.step-num{position:absolute;top:2px;width:64px;height:64px;background:var(--dark);color:var(--white);font-weight:700;font-size:22px;display:flex;align-items:center;justify-content:center}
.step-left{left:115px;width:259px}
.step-left .step-text{position:absolute;left:0;top:0;width:182px;height:72px}
.step-left .step-num{left:195px}
.step-right{left:400px;width:272px}
.step-right .step-num{left:0}
.step-right .step-text{position:absolute;left:72px;top:0;width:200px;height:72px}
.info-form{position:absolute;top:772px;left:115px;width:555px;height:92px;background:var(--yellow);border-radius:10px;display:flex;align-items:center;padding:0 20px;gap:18px}
.info-form .car-icon{width:64px;height:40px}
.info-form h2{font-size:15px;font-weight:700;width:150px}
.fields{display:flex;flex-direction:column;gap:8px}
.fields span{display:block;width:150px;height:18px;background:var(--white);border-radius:3px;font-size:8px;color:#999;padding:3px 6px}
.submit{background:#111;color:var(--white);font-weight:700;font-size:14px;padding:10px 14px}
.promo-bar{position:absolute;top:882px;left:115px;width:555px;height:34px;background:var(--yellow);border-radius:6px;font-size:15px;font-weight:700;padding:6px 14px}
.testimonial{position:absolute;top:935px;left:0;width:774px;height:133px;background:linear-gradient(90deg,#2b2522,#4a3f37)}
.avatar{position:absolute;left:160px;top:28px;width:50px;height:50px;border-radius:50%;background:#b9aa9c}
.arrow{position:absolute;top:42px}
.quote{position:absolute;left:232px;top:26px;width:380px;font-size:9.5px;line-height:1.5;color:#eee}
.quote-by{position:absolute;right:140px;top:102px;font-size:9px;color:#eee}
.site-footer{position:absolute;top:1068px;left:0;width:774px;height:118px;background:var(--blue);color:var(--white)}
.footer-col{position:absolute;top:14px;font-size:8.5px;line-height:1.6}
.footer-col h4{font-size:10px;font-weight:700;margin-bottom:4px}
.footer-col ul{list-style:none}
.social li{display:flex;align-items:center;gap:5px}
.social li::before{content:"";width:9px;height:9px;border-radius:50%;background:var(--white)}
.footer-brand{position:absolute;right:50px;top:30px;display:flex;flex-direction:column;align-items:flex-start}
.footer-brand .row{display:flex;align-items:center;gap:8px}
.footer-brand .brand-dot{width:30px;height:30px}
.footer-brand .brand-name{color:var(--yellow);font-size:26px}
.tagline{font-size:9px;margin-left:38px}
.copyright{position:absolute;top:1186px;left:0;width:774px;height:14px;background:#1e87b3;color:var(--white);font-size:7px;text-align:center;line-height:14px}
</style>
</head>
<body>
<header class="site-header">
  <div class="brand"><span class="brand-dot"></span><span class="brand-name">Tollo</span></div>
  <div class="header-phone">555-014-2290</div>
  <nav class="main-nav">
    <a href="#">Home</a><a href="#">About Us</a><a href="#">Tollo Certified</a><a href="#">Why Tollo</a><a href="#">FAQs</a><a href="#">Contact Us</a>
  </nav>
</header>

<section class="hero">
  <div class="hero-photo" role="img" aria-label="Close-up photo of a classic car's chrome front"></div>
</section>

<section class="intro">
  <h1>Lorem ipsum is a dummy</h1>
  <p>Lorem Ipsum is simply dummy text of the printing and typesetting industry. Lorem Ipsum has been the industry's standard dummy text ever since the 1500s, when an unknown printer took a galley of type and scrambled it to make a type specimen book. It has survived not only five centuries, but also the leap into electronic typesetting, remaining essentially unchanged. It was popularised in the 1960s with the release of sheets containing passages.</p>
</section>

<section class="features">
  <div class="feature-photo" role="img" aria-label="Photo of a driver seated in a car"></div>
  <ul class="feature-list">
    <li>Lorem ipsum is simply dummy text</li>
    <li>Lorem ipsum is simply dummy text</li>
    <li>Lorem ipsum is simply dummy text</li>
    <li>Lorem ipsum is simply dummy text</li>
    <li>Lorem ipsum is simply dummy text</li>
    <li>Lorem ipsum is simply dummy text</li>
  </ul>
</section>

<section class="steps">
  <div class="step step-left" style="top:28px">
    <div class="step-text"><h3>Lorem ipsum is dummy</h3><p>Lorem Ipsum is simply dummy text of the printing and typesetting industry, standard dummy text ever since it was made.</p><span class="more">Read more...</span></div>
    <div class="step-num">.01</div>
  </div>
  <div class="step step-right" style="top:28px">
    <div class="step-num">.02</div>
    <div class="step-text"><h3>Lorem ipsum is dummy</h3><p>Lorem Ipsum is simply dummy text of the printing and typesetting industry, standard dummy text ever since it was made.</p><span class="more">Read more...</span></div>
  </div>
  <div class="step step-left" style="top:110px">
    <div class="step-text"><h3>Lorem ipsum is dummy</h3><p>Lorem Ipsum is simply dummy text of the printing and typesetting industry, standard dummy text ever since it was made.</p><span class="more">Read more...</span></div>
    <div class="step-num">.03</div>
  </div>
  <div class="step step-right" style="top:110px">
    <div class="step-num">.04</div>
    <div class="step-text"><h3>Lorem ipsum is dummy</h3><p>Lorem Ipsum is simply dummy text of the printing and typesetting industry, standard dummy text ever since it was made.</p><span class="more">Read more...</span></div>
  </div>
</section>

<section class="info-form">
  <svg class="car-icon" viewBox="0 0 64 40" aria-hidden="true">
    <path d="M8 22 L16 8 H48 L56 22 H60 V32 H4 V22 Z" fill="#111"/>
    <rect x="18" y="12" width="28" height="9" fill="#ffc214"/>
    <circle cx="16" cy="27" r="3" fill="#ffc214"/><circle cx="48" cy="27" r="3" fill="#ffc214"/>
    <rect x="8" y="32" width="8" height="6" fill="#111"/><rect x="48" y="32" width="8" height="6" fill="#111"/>
  </svg>
  <h2>Tollo info form</h2>
  <div class="fields"><span>Name</span><span>Email</span></div>
  <div class="submit">Submit</div>
</section>

<div class="promo-bar">Lorem ipsum is simply dummy text of the printing...</div>

<section class="testimonial">
  <svg class="arrow" style="left:128px" width="14" height="20" viewBox="0 0 14 20" aria-hidden="true"><path d="M11 2 L3 10 L11 18" stroke="#fff" stroke-width="2.5" fill="none"/></svg>
  <div class="avatar" role="img" aria-label="Customer portrait"></div>
  <p class="quote">Lorem ipsum dolor sit amet, ultricies adipiscing elit. Metus tellus nam, vestibule quis dapibus non, porttitor ornare ligula. Dui mauris convallis porttitor, sit amet lorem turpis lacinia vitae, felis id nam metus, vestibulum.</p>
  <p class="quote-by">– Visit website</p>
  <svg class="arrow" style="left:632px" width="14" height="20" viewBox="0 0 14 20" aria-hidden="true"><path d="M3 2 L11 10 L3 18" stroke="#fff" stroke-width="2.5" fill="none"/></svg>
</section>

<footer class="site-footer">
  <div class="footer-col" style="left:115px">
    <h4>Quick links</h4>
    <ul><li>About us</li><li>Services</li><li>Become</li><li>Sitemap</li><li>Contact Us</li></ul>
  </div>
  <div class="footer-col social" style="left:240px">
    <h4>Follow Us</h4>
    <ul><li>Friendly</li><li>Chirper</li><li>Workline</li></ul>
  </div>
  <div class="footer-col" style="left:380px">
    <h4>Contact us</h4>
    <ul><li>48 Harbor Lane Suite 12</li><li>Dunmore, TX 75001</li><li>Tel: 555-014-2290</li><li>hello@tollo.example</li></ul>
  </div>
  <div class="footer-brand">
    <div class="row"><span class="brand-dot"></span><span class="brand-name">Tollo</span></div>
    <span class="tagline">Your Tagline Here</span>
  </div>
</footer>
<div class="copyright">© 2017 Tollo. All rights reserved.</div>
</body>
</html>
```